Real Estate Investor needs awesome business card design

I invest in real estate, focused on multi-family properties, and I need a business card to hand out to potential partners. I prefer simple, clean designs, but it needs to stand out, so I'd like there to be a bit of red in the design as well.

It should include this information:

Front
Dallin Pecksworth
Real Estate Investor
Direct phone: 502-867-3394
Email: dallinhpecksworth@quillmail.example
Headshot (Picture), I've uploaded a few, just pick the one you think looks best with your design. You can remove the background from the headshot image if it looks better.

Back
The back of the card's design should flow and be congruent with the front. On the back I want to put an inspirational quote or question. There will be different ones depending on the card, so I'll need the original file so I can edit it in the end.

For now, use “The Pessimist Sees Difficulty In Every Opportunity. The Optimist Sees The Opportunity In Every Difficulty.” -Barnaby Ellsworth

Target Market(s)

Investors

Industry/Entity Type

Real Estate

Contact Information for Business Card

Front
Dallin Pecksworth
Real Estate Investor

Back
The back of the card's design should flow and be congruent with the front. On the back I want to put an inspirational quote or question. There will be different ones depending on the card, so I'll need the original file so I can edit it in the end. I've uploaded some EXAMPLES of business cards with quotes on them. Don't copy but feel free to use them as inspiration.

The design will be printed on "ZIB sized" business cards
1039 x 697 pixels
with rounded corners

Font styles to use
Serif
Decorative
Script

Colors
ec1f27

Requirements
Must have
• Headshot, name, and other information in it.
• 1039 x 697 pixels
• Rounded corners
• Clean design that pops. I'm open to see any color background, including black.
• Headshots can be located here: https://www.filecrate.example/sh/8kd2wq7mzt31hvx/BBQTXP4ruf9LmQ0KhcvWx7b?dl=0
Nice to have
• It would be awesome if the design included a personal signature or monogram, but if not I'll get a personal logo developed later and the card redesigned if I think it needs it.
Should not have
• Cluttered design

```html
<!DOCTYPE html>
<html lang="en">
<head>
<meta charset="utf-8">
<title>Dallin Pecksworth – Business Card</title>
<link rel="stylesheet" href="https://fonts.googleapis.com/css2?family=Ubuntu:ital,wght@0,400;0,500;0,700;1,400&display=swap">
<style>
  :root {
    --page-bg: #eef0f4;
    --card-white: #ffffff;
    --brand-blue: #3d5ba3;
    --name-blue: #2f4f9c;
    --brand-red: #ec1f27;
    --accent-light: #b8cbf3;
    --ink: #1d1d1f;
    --photo-light: #f4f5f7;
    --photo-mid: #c9ced8;
    --photo-dark: #2a3146;
    --rule: rgba(255,255,255,0.75);
  }
  * { box-sizing: border-box; margin: 0; padding: 0; }
  html, body {
    width: 1200px; height: 898px; overflow: hidden;
    background: var(--page-bg);
    font-family: "Ubuntu", sans-serif;
  }
  .sheet {
    position: relative; width: 1200px; height: 898px;
    display: flex; flex-direction: column; align-items: center; justify-content: center; gap: 28px;
  }
  .card {
    position: relative; width: 620px; height: 415px;
    border-radius: 22px; overflow: hidden;
    box-shadow: 0 6px 18px rgba(20,30,60,0.18);
  }
  /* Front */
  .card-front { background: var(--card-white); }
  .identity {
    position: absolute; left: 48px; top: 128px;
    border-left: 3px solid var(--brand-red); padding-left: 12px;
    z-index: 1;
  }
  .identity-name { font-size: 27px; font-weight: 700; color: var(--name-blue); line-height: 1.1; white-space: nowrap; }
  .identity-title { font-size: 15px; font-weight: 400; color: var(--ink); margin-top: 2px; }
  .contact {
    position: absolute; left: 60px; top: 262px;
    font-size: 12.5px; color: var(--ink); line-height: 1.45;
    white-space: nowrap; z-index: 1;
  }
  .contact-value { color: var(--name-blue); }
  .headshot {
    position: absolute; right: 0; top: 0; width: 250px; height: 100%;
    background:
      linear-gradient(180deg, transparent 60%, var(--photo-dark) 100%),
      linear-gradient(90deg, var(--card-white) 0%, var(--photo-light) 25%, var(--photo-mid) 100%);
  }
  /* Back */
  .card-back { background: var(--brand-blue); color: var(--card-white); }
  .quote {
    position: absolute; left: 62px; top: 96px; width: 520px;
    font-size: 25px; font-weight: 700; line-height: 36px;
  }
  .quote-mark {
    color: var(--accent-light); font-size: 58px; font-weight: 700;
    line-height: 0; vertical-align: -20px;
  }
  .quote-mark-open { margin-right: 6px; }
  .quote-mark-close { margin-left: 10px; }
  .quote-accent { color: var(--accent-light); }
  .quote-author {
    position: absolute; right: 70px; top: 246px;
    font-size: 12px; font-style: italic; font-weight: 400;
  }
  .quote-rule {
    position: absolute; left: 62px; right: 40px; top: 272px;
    height: 1px; background: var(--rule);
  }
  .quote-rule::after {
    content: ""; position: absolute; left: 0; top: -1px;
    width: 40px; height: 3px; background: var(--brand-red);
  }
</style>
</head>
<body>
<main class="sheet">
  <section class="card card-front">
    <div class="headshot" role="img" aria-label="Headshot of Dallin Pecksworth in a dark suit jacket and white shirt"></div>
    <div class="identity">
      <h1 class="identity-name">Dallin Pecksworth</h1>
      <p class="identity-title">Real Estate Investor</p>
    </div>
    <div class="contact">
      <p>Direct phone: <span class="contact-value">502-867-3394</span></p>
      <p>Email: <span class="contact-value">dallinhpecksworth</span>@quillmail.example</p>
    </div>
  </section>

  <section class="card card-back">
    <p class="quote">
      <span class="quote-mark quote-mark-open">“</span>The <span class="quote-accent">Pessimist Sees Difficulty</span><br>
      In Every Opportunity. <span class="quote-accent">The Optimist</span><br>
      <span class="quote-accent">Sees The Opportunity</span> In Every<br>
      Difficulty.<span class="quote-mark quote-mark-close">”</span>
    </p>
    <p class="quote-author">- Barnaby Ellsworth</p>
    <div class="quote-rule"></div>
  </section>
</main>
</body>
</html>
```